Ridgeline Yard Works Stationary Package
Business Cards, Letterhead, Envelope, Sticker, Fax Cover sheet, invoice, and estimate
Ridgeline Yard Works Stationary Package - Construction
Creative Brief
Use same font as used in my logo
Pete Marrow
Owner
4172 W. Fenwick Rd. Burbank, IL 60421
petemarrow@quailnet.example
www.ridgelineyardworks.example
Can information be in a format that can be edited for future use. ex: Name Changes, New Numbers, etc?

```html
<!DOCTYPE html>
<html lang="en">
<head>
<meta charset="utf-8">
<title>Ridgeline Yard Works – Business Card</title>
<link rel="stylesheet" href="https://fonts.googleapis.com/css2?family=Michroma&family=Saira:wght@400;500&family=Open+Sans:wght@400;600&display=swap">
<style>
  :root {
    --page-bg: #e9e7e3;
    --card-white: #ffffff;
    --ink-dark: #2b2b30;
    --ink-grey: #4a4a50;
    --navy-deep: #17265e;
    --navy-mid: #24398a;
    --navy-glow: #3c64b8;
    --accent-red: #c1121f;
    --text-light: #ffffff;
    --text-soft: #dfe6f5;
  }
  * { margin: 0; padding: 0; box-sizing: border-box; }
  html, body {
    width: 1200px; height: 778px; overflow: hidden;
    background: var(--page-bg);
  }
  .business-card {
    position: absolute; left: 60px; top: 122px;
    width: 1080px; height: 534px;
    border-radius: 34px; overflow: hidden;
    background: var(--card-white);
    box-shadow: 0 6px 18px rgba(0,0,0,0.18);
  }
  .card-art { position: absolute; inset: 0; }
  .brand {
    position: absolute; left: 144px; top: 40px;
    display: flex; align-items: center; gap: 28px;
  }
  .brand-square {
    width: 126px; height: 126px; border-radius: 18px;
    background: var(--navy-mid);
  }
  .brand-text { display: flex; flex-direction: column; align-items: center; }
  .brand-name {
    font-family: "Michroma", sans-serif;
    font-size: 42px; color: var(--ink-dark);
    letter-spacing: 0.3px; white-space: nowrap;
  }
  .brand-tagline {
    display: flex; align-items: center; gap: 14px; margin-top: 6px;
    font-family: "Saira", sans-serif; font-size: 26px; color: var(--ink-grey);
    white-space: nowrap;
  }
  .brand-tagline::before, .brand-tagline::after {
    content: ""; width: 70px; height: 2px; background: var(--ink-grey);
  }
  .person {
    position: absolute; right: 620px; top: 362px;
    text-align: right; font-family: "Open Sans", sans-serif;
  }
  .person-name { font-size: 34px; font-weight: 600; color: var(--text-light); line-height: 1.2; }
  .person-role { font-size: 24px; font-weight: 600; color: var(--text-soft); line-height: 1.2; }
  .divider {
    position: absolute; left: 525px; top: 300px;
    width: 2px; height: 210px;
    background: linear-gradient(to bottom, rgba(255,255,255,0), rgba(255,255,255,0.6), rgba(255,255,255,0));
  }
  .contact {
    position: absolute; left: 576px; top: 318px;
    font-family: "Open Sans", sans-serif; font-size: 21px;
    color: var(--text-light); line-height: 28px;
  }
  .address { margin-bottom: 10px; }
  .contact-line { display: flex; align-items: center; gap: 12px; white-space: nowrap; }
  .contact-line svg { width: 18px; height: 18px; flex: none; }
</style>
</head>
<body>
  <div class="business-card">
    <svg class="card-art" viewBox="0 0 1080 534" preserveAspectRatio="none" aria-hidden="true">
      <defs>
        <radialGradient id="navyGlow" cx="0.5" cy="0.62" r="0.6">
          <stop offset="0" stop-color="#3c64b8"/>
          <stop offset="0.55" stop-color="#24398a"/>
          <stop offset="1" stop-color="#17265e"/>
        </radialGradient>
      </defs>
      <path d="M0,158 Q540,316 1080,158 L1080,178 Q540,330 0,178 Z" fill="var(--accent-red)"/>
      <path d="M0,178 Q540,330 1080,178 L1080,534 L0,534 Z" fill="url(#navyGlow)"/>
    </svg>

    <div class="brand">
      <div class="brand-square"></div>
      <div class="brand-text">
        <div class="brand-name">Ridgeline Yard Works</div>
        <div class="brand-tagline">Home Restoration Specialists</div>
      </div>
    </div>

    <div class="person">
      <div class="person-name">Pete Marrow</div>
      <div class="person-role">Owner</div>
    </div>

    <div class="divider"></div>

    <div class="contact">
      <div class="address">4172 W. Fenwick Rd.<br>Alder Falls, MN 55021</div>
      <div class="contact-line">
        <svg viewBox="0 0 20 20"><rect x="6" y="2" width="8" height="16" rx="2" fill="none" stroke="#fff" stroke-width="2"/><circle cx="10" cy="15" r="1" fill="#fff"/></svg>
        (555) 201-0142
      </div>
      <div class="contact-line">
        <svg viewBox="0 0 20 20"><rect x="3" y="7" width="14" height="10" rx="2" fill="#fff"/><rect x="6" y="3" width="8" height="5" fill="none" stroke="#fff" stroke-width="1.6"/></svg>
        (555) 201-0187
      </div>
      <div class="contact-line">
        <svg viewBox="0 0 20 20"><rect x="2" y="5" width="16" height="11" rx="1" fill="none" stroke="#fff" stroke-width="1.8"/><path d="M2 6 L10 12 L18 6" fill="none" stroke="#fff" stroke-width="1.8"/></svg>
        petemarrow@quailnet.example
      </div>
      <div class="contact-line">
        <svg viewBox="0 0 20 20"><circle cx="10" cy="10" r="8" fill="none" stroke="#fff" stroke-width="1.8"/><path d="M2 10 H18 M10 2 Q5 10 10 18 Q15 10 10 2" fill="none" stroke="#fff" stroke-width="1.5"/></svg>
        www.ridgelineyardworks.example
      </div>
    </div>
  </div>
</body>
</html>
```